Modern Spot UV Business Card design

We are a relatively new real estate agency. We need a business card that reflects the professionalism and prestige of our company but is also modern and fresh, based around our logo.
We would love to utilise spot UV.
Happy to let the designers use their imagination and see what they come up with (we're not very creative, so have no ideas for you, sorry) :-)
We'd like one for each staff member, but I've just provided one staff members photo here to avoid confusion.

Target Market(s)

Families

Industry/Entity Type

Real Estate Agent

Contact Information for Business Card

Colin Varga - Director & Principal
Mobile: 0491 527 806
Email: colin.varga@vbrokers.example.com.au
Phone: (08) 7364 9150
Fax: (08) 7364 9182
www.vargabrokersrealestate.example.com.au

Font styles to use
Other font styles liked:
• Kabel Dm BT

Requirements
Must have
• Contact details, logo, photo, spot UV
Nice to have
• Modern interesting features that will make people comment. Nothing too feminine nor too masculine.
Should not have
• No houses! Nothing typical of a real estate agent.

```html
<!DOCTYPE html>
<html lang="en">
<head>
<meta charset="utf-8">
<title>Varga Brokers Real Estate – Business Card</title>
<link rel="stylesheet" href="https://fonts.googleapis.com/css2?family=Open+Sans:wght@300;400;700&display=swap">
<style>
  :root {
    --canvas: #e9e6e1;
    --card-white: #ffffff;
    --card-black: #111213;
    --ink-dark: #3a3b3d;
    --ink-grey: #7a7c80;
    --accent-blue: #1ea0dc;
    --accent-orange: #f5a21b;
    --text-light: #f2f2f2;
    --uv-gloss: #3a3d42;
    --photo-light: #e3e5e8;
    --photo-dark: #6d7177;
  }
  * { margin: 0; padding: 0; box-sizing: border-box; }
  html, body {
    width: 1200px; height: 1023px; overflow: hidden;
    background: var(--canvas);
    font-family: "Open Sans", Arial, sans-serif;
  }
  .canvas { position: relative; width: 1200px; height: 1023px; }
  .card {
    position: absolute; left: 250px; width: 700px; height: 428px;
    border-radius: 22px; overflow: hidden;
    box-shadow: 0 10px 28px rgba(0,0,0,.22);
  }
  .card--front { top: 50px; background: var(--card-white); }
  .card--back { top: 535px; background: var(--card-black); }
  .card svg.card-art { position: absolute; inset: 0; }

  .logo { position: absolute; display: flex; align-items: center; gap: 12px; }
  .logo__mark { width: 26px; height: 26px; border-radius: 50%; background: var(--accent-orange); }
  .logo__name { font-weight: 700; font-size: 40px; letter-spacing: -0.5px; line-height: 1; }
  .logo-sub { position: absolute; display: flex; align-items: center; gap: 10px; }
  .logo-sub__estate { font-weight: 300; font-size: 30px; line-height: 1; }
  .logo-sub__tagline { font-size: 12px; line-height: 1.15; padding-left: 10px; border-left: 1px solid currentColor; }

  .card--front .logo { left: 46px; top: 110px; color: var(--ink-dark); }
  .card--front .logo-sub { left: 48px; top: 158px; color: var(--ink-grey); }

  .contact { position: absolute; left: 46px; top: 282px; color: var(--text-light); }
  .contact__name { color: var(--accent-blue); font-size: 21px; font-weight: 400; line-height: 1.1; }
  .contact__role { font-size: 14px; margin-bottom: 8px; }
  .contact__list { list-style: none; font-size: 14px; line-height: 19px; }
  .contact__list li { display: flex; align-items: center; gap: 10px; }
  .contact__icon { width: 12px; height: 12px; flex: none; }

  .card--back .logo { left: 190px; top: 150px; color: var(--uv-gloss); }
  .card--back .logo__mark { background: var(--uv-gloss); }
  .card--back .logo-sub { left: 192px; top: 198px; color: var(--uv-gloss); }
  .website {
    position: absolute; left: 0; right: 0; top: 300px; text-align: center;
    color: #c9cbcf; font-size: 15px; letter-spacing: 4px;
  }
  .website__domain { color: var(--accent-blue); }
</style>
</head>
<body>
<main class="canvas">

  <section class="card card--front" aria-label="Business card front">
    <svg class="card-art" width="700" height="428" viewBox="0 0 700 428">
      <defs>
        <linearGradient id="photoTone" x1="0" y1="0" x2="1" y2="1">
          <stop offset="0" stop-color="var(--photo-light)"/>
          <stop offset="1" stop-color="var(--photo-dark)"/>
        </linearGradient>
        <linearGradient id="orangeFade" x1="0" y1="0" x2="1" y2="0">
          <stop offset="0.45" stop-color="#f5a21b" stop-opacity="0"/>
          <stop offset="1" stop-color="#f5a21b"/>
        </linearGradient>
      </defs>
      <rect class="portrait" role="img" aria-label="Portrait photo of the agent in a grey suit" x="420" y="0" width="280" height="220" fill="url(#photoTone)"/>
      <path class="wave-orange" d="M0,250 C200,250 300,212 420,144 S620,50 700,42 L700,66 C620,74 540,104 420,174 S200,276 0,276 Z" fill="url(#orangeFade)"/>
      <path class="wave-blue" d="M0,262 C200,262 300,224 420,156 S620,64 700,56 L700,428 L0,428 Z" fill="var(--accent-blue)"/>
      <path class="wave-black" d="M0,270 C200,270 300,232 420,164 S620,72 700,64 L700,428 L0,428 Z" fill="var(--card-black)"/>
    </svg>

    <div class="logo"><span class="logo__name">Varga Brokers</span><span class="logo__mark"></span></div>
    <div class="logo-sub"><span class="logo-sub__estate">Real Estate</span><span class="logo-sub__tagline">Opening doors to<br>your new chapter</span></div>

    <div class="contact">
      <p class="contact__name">Colin Varga</p>
      <p class="contact__role">Director &amp; Principal</p>
      <ul class="contact__list">
        <li><svg class="contact__icon" viewBox="0 0 12 12"><rect width="12" height="12" rx="2" fill="var(--accent-blue)"/><rect x="4" y="2" width="4" height="8" rx="1" fill="var(--card-black)"/></svg>0491 527 806</li>
        <li><svg class="contact__icon" viewBox="0 0 12 12"><rect width="12" height="12" rx="2" fill="var(--accent-blue)"/><path d="M3 3h2l1 2-1 1a4 4 0 0 0 2 2l1-1 2 1v2a1 1 0 0 1-1 1A7 7 0 0 1 2 4a1 1 0 0 1 1-1z" fill="var(--card-black)"/></svg>(08) 7364 9150</li>
        <li><svg class="contact__icon" viewBox="0 0 12 12"><rect width="12" height="12" rx="2" fill="var(--accent-blue)"/><rect x="2.5" y="5" width="7" height="4.5" fill="var(--card-black)"/><rect x="4" y="2.5" width="4" height="2.5" fill="var(--card-black)"/></svg>(08) 7364 9182</li>
        <li><svg class="contact__icon" viewBox="0 0 12 12"><rect width="12" height="12" rx="2" fill="var(--accent-blue)"/><rect x="2" y="3.5" width="8" height="5" fill="var(--card-black)"/><path d="M2 3.5l4 3 4-3" stroke="var(--accent-blue)" fill="none"/></svg>colin.varga@vbrokers.example.com.au</li>
      </ul>
    </div>
  </section>

  <section class="card card--back" aria-label="Business card back">
    <div class="logo"><span class="logo__name">Varga Brokers</span><span class="logo__mark"></span></div>
    <div class="logo-sub"><span class="logo-sub__estate">Real Estate</span><span class="logo-sub__tagline">Opening doors to<br>your new chapter</span></div>
    <p class="website">www.<span class="website__domain">vbrokers</span>.example.com.au</p>
  </section>

</main>
</body>
</html>
```